BANNER PUBBLICITARIO FACEBOOK

Advertise our services via facebook.
We are a medical center of diagnostic imaging, perform MRI, CT, ultrasound and specialist visits. I want to advertise our center through Facebook trying to get the knowledge of our center to as many people as possible. our target audience are people from 18 to 80 years old.
I want to highlight our contact details, our address and our website www. corvalux.it. All contact information can be found on our website

Target Market(s)

my target market are people from 18 to 80 years old who have to perform diagnostic tests such as magnetic resonance imaging tac ultrasound etc

Colors
0054AA
0677BA
7BADD7
CADEEF
E8F1F8
0094D4
00A9DD
6FCCEA
C7EBF8
E9F6FB
00AB8E
00BBA5
67D7C9
C6EFE9
E9F9F6

Requirements
Must have
• my project should be impactful and attractive. When the user sees my post he must be attracted
Nice to have
• I would like to highlight our diagnostic machines, so that the customers understand immediately what we are doing. As indicated on our website www.corvalux.it

```html
<!DOCTYPE html>
<html lang="en">
<head>
<meta charset="utf-8">
<title>Corvalux Healthcare Diagnostic Center</title>
<link href="https://fonts.googleapis.com/css2?family=Archivo:wght@700;800;900&family=Poppins:wght@500;600;700&display=swap" rel="stylesheet">
<style>
  :root {
    --blue-deep: #0054AA;
    --blue: #0677BA;
    --blue-text: #16639a;
    --teal: #00AB8E;
    --teal-bright: #00BBA5;
    --sky-soft: #E9F6FB;
    --sky-mid: #C7EBF8;
    --sky: #6FCCEA;
    --ink: #0b0b0b;
    --white: #ffffff;
  }
  * { margin: 0; padding: 0; box-sizing: border-box; }
  html, body { width: 1200px; height: 1200px; overflow: hidden; background: var(--sky-soft); }
  .banner {
    position: relative;
    width: 1200px;
    height: 1200px;
    overflow: hidden;
    background: linear-gradient(135deg, #f1f9fd 0%, var(--sky-soft) 45%, #d6eef8 100%);
    font-family: "Poppins", sans-serif;
  }
  .banner__shapes { position: absolute; inset: 0; width: 1200px; height: 1200px; }
  .brand {
    position: absolute;
    left: 64px;
    top: 88px;
    display: flex;
    align-items: center;
    gap: 18px;
    font-family: "Poppins", sans-serif;
    font-weight: 600;
    font-size: 74px;
    line-height: 1;
    color: var(--blue);
  }
  .brand__dot { width: 26px; height: 26px; border-radius: 50%; background: var(--teal); }
  .headline { position: absolute; left: 60px; top: 222px; font-family: "Archivo", sans-serif; }
  .headline__top {
    font-weight: 800;
    font-size: 57px;
    letter-spacing: -0.5px;
    color: var(--blue);
    line-height: 1;
  }
  .headline__main {
    font-weight: 900;
    font-size: 164px;
    letter-spacing: -2px;
    color: var(--teal);
    line-height: 1;
    margin-top: 14px;
  }
  .tagline {
    position: absolute;
    left: 60px;
    top: 454px;
    font-family: "Archivo", sans-serif;
    font-weight: 700;
    font-size: 32px;
    letter-spacing: -0.4px;
    color: var(--ink);
  }
  .benefits { position: absolute; left: 68px; top: 530px; list-style: none; }
  .benefits__item {
    display: flex;
    align-items: center;
    gap: 28px;
    height: 52px;
    margin-bottom: 26px;
    font-weight: 600;
    font-size: 29px;
    color: var(--blue-text);
  }
  .benefits__icon { width: 52px; height: 52px; flex: none; }
  .contact-label {
    position: absolute;
    left: 47px;
    top: 814px;
    width: 261px;
    height: 44px;
    border-radius: 22px;
    background: var(--teal);
    color: var(--white);
    font-family: "Archivo", sans-serif;
    font-weight: 700;
    font-size: 28px;
    letter-spacing: -0.3px;
    display: flex;
    align-items: center;
    justify-content: center;
  }
  .contact { position: absolute; left: 71px; top: 893px; font-style: normal; }
  .contact__line {
    display: block;
    font-weight: 600;
    font-size: 24px;
    line-height: 1;
    color: var(--blue-text);
    margin-bottom: 23px;
  }
  .contact__address { line-height: 1.5; }
</style>
</head>
<body>
<main class="banner">
  <svg class="banner__shapes" viewBox="0 0 1080 1080" xmlns="http://www.w3.org/2000/svg" aria-hidden="false">
    <defs>
      <linearGradient id="tile-sky" x1="0" y1="0" x2="1" y2="1">
        <stop offset="0" stop-color="#8fd0e4"/>
        <stop offset="1" stop-color="#5fb6d3"/>
      </linearGradient>
      <linearGradient id="tile-pale" x1="0" y1="0" x2="1" y2="1">
        <stop offset="0" stop-color="#c9e9f4"/>
        <stop offset="1" stop-color="#7fc3db"/>
      </linearGradient>
      <linearGradient id="scanner-room" x1="0" y1="0" x2="1" y2="1">
        <stop offset="0" stop-color="#f4f6f8"/>
        <stop offset="0.6" stop-color="#e3e8ec"/>
        <stop offset="1" stop-color="#cfe2ee"/>
      </linearGradient>
      <linearGradient id="xray-review" x1="0" y1="0" x2="1" y2="1">
        <stop offset="0" stop-color="#e6ecef"/>
        <stop offset="0.5" stop-color="#c8d2d8"/>
        <stop offset="1" stop-color="#e8d3c6"/>
      </linearGradient>
    </defs>
    <rect x="820" y="40" width="380" height="380" rx="70" transform="rotate(45 1010 230)" fill="url(#tile-sky)" opacity="0.85"/>
    <rect x="700" y="440" width="520" height="520" rx="80" transform="rotate(45 960 700)" fill="url(#tile-pale)" opacity="0.8"/>
    <rect x="820" y="820" width="420" height="420" rx="70" transform="rotate(45 1030 1030)" fill="url(#tile-sky)" opacity="0.9"/>
    <rect x="430" y="720" width="250" height="250" rx="50" transform="rotate(45 555 845)" fill="url(#tile-pale)" opacity="0.7"/>
    <g role="img" aria-label="Photo of a white MRI scanner with a blue patient table">
      <rect x="685" y="490" width="400" height="400" rx="60" transform="rotate(45 885 690)" fill="url(#scanner-room)" stroke="#ffffff" stroke-width="12"/>
    </g>
    <g role="img" aria-label="Blurred photo of a doctor reviewing an X-ray film">
      <rect x="420" y="830" width="380" height="380" rx="60" transform="rotate(45 610 1020)" fill="url(#xray-review)" stroke="#ffffff" stroke-width="12"/>
    </g>
  </svg>

  <div class="brand"><span class="brand__dot"></span>Corvalux</div>

  <h1 class="headline">
    <span class="headline__top">HEALTHCARE DIAGNOSTIC</span><br>
    <span class="headline__main">CENTER</span>
  </h1>

  <p class="tagline">Pioneers in diagnostic practice</p>

  <ul class="benefits">
    <li class="benefits__item">
      <svg class="benefits__icon" viewBox="0 0 52 52"><circle cx="26" cy="26" r="26" fill="#00AB8E"/><path d="M15 27l8 8 15-17" fill="none" stroke="#fff" stroke-width="6" stroke-linecap="round" stroke-linejoin="round"/></svg>
      Specialize Modern Equipment
    </li>
    <li class="benefits__item">
      <svg class="benefits__icon" viewBox="0 0 52 52"><circle cx="26" cy="26" r="26" fill="#00AB8E"/><path d="M15 27l8 8 15-17" fill="none" stroke="#fff" stroke-width="6" stroke-linecap="round" stroke-linejoin="round"/></svg>
      We treat all people with care
    </li>
    <li class="benefits__item">
      <svg class="benefits__icon" viewBox="0 0 52 52"><circle cx="26" cy="26" r="26" fill="#00AB8E"/><path d="M15 27l8 8 15-17" fill="none" stroke="#fff" stroke-width="6" stroke-linecap="round" stroke-linejoin="round"/></svg>
      Best Experience
    </li>
  </ul>

  <div class="contact-label">CONTACT US</div>

  <address class="contact">
    <span class="contact__line">0549-734208</span>
    <span class="contact__line">Mon-Fri 8:00-19:00</span>
    <span class="contact__line">info@corvalux.it</span>
    <span class="contact__line contact__address">Lauretana Road, 17<br>47893, Valdoria, RSM</span>
  </address>
</main>
</body>
</html>
```